Financial Retirement Seminar Mailer

We would like to redesign our mailer flyer so that it looks classier and more effective in attracting people to sign up for our events. We help people who are near or in retirement achieve their financial goals.

PLEASE CHANGE THE ENTIRE FORMAT OF THE FLYER AND DO NOT LET IT LOOK SIMILAR TO WHAT WE CURRENTLY HAVE. NOTHING HAS TO STAY THE SAME. THE MORE UNIQUE YOU ARE THE HIGHER YOUR CHANCES OF WINNING.
ALL IMAGES CAN BE CHANGED (except Dorian Vell's photo and the logo for Marlow's Tavern Grill)

Target Market(s)

Our Target Market are upper middle class adults nearing or in retirement ages 55+.

Industry/Entity Type

Finance

Font styles to use
Serif
Sans Serif

Colors
0255a3
fece3e
ffffff

Requirements
Must have
• -Must have a photo of Dorian Vell and logo of Marlows Tavern. All other images can be changed.
• -Use our company colors which are navy and GOLD (Please use gold gradients instead of just yellow color)
• -The flyer must be folded in half. The inside can be full page.
Nice to have
• -If you could make the gold color stand out somehow maybe a gradient gold.

```html
<!DOCTYPE html>
<html lang="en">
<head>
<meta charset="utf-8">
<title>Advanced Retirement Solutions – Seminar Mailer</title>
<link href="https://fonts.googleapis.com/css2?family=Marcellus&family=Source+Sans+3:wght@300;400;600;700&display=swap" rel="stylesheet">
<style>
:root{
  --navy:#1d3c84;
  --navy-deep:#142d68;
  --blue:#0255a3;
  --gold:#f2b400;
  --gold-light:#fce58c;
  --gold-text:#e9a900;
  --white:#ffffff;
  --paper:#f0f0f2;
  --ink:#1f2a44;
  --stage:#e6e6e8;
  --gold-grad:linear-gradient(90deg,#d99a00 0%,#f6c52a 30%,#fde89a 55%,#f2b400 80%,#d99a00 100%);
}
*{box-sizing:border-box;margin:0;padding:0}
html,body{width:1200px;height:801px;overflow:hidden;background:var(--stage)}
body{position:relative;font-family:"Source Sans 3",Arial,sans-serif;color:var(--ink)}
.panel{position:absolute;top:84px;width:461px;height:634px;background:var(--paper);overflow:hidden;box-shadow:0 3px 10px rgba(0,0,0,.18)}
.panel--outside{left:120px}
.panel--inside{left:619px;background:var(--white)}
.abs{position:absolute}
.serif{font-family:"Marcellus",Georgia,serif}
.gold-text{color:var(--gold-text)}

/* footer band */
.footer-band{position:absolute;left:0;bottom:0;width:461px;height:80px}
.footer-copy{position:absolute;left:14px;bottom:12px;color:var(--white)}
.footer-copy h3{font-family:"Source Sans 3",sans-serif;font-weight:600;font-size:17px;color:var(--gold);letter-spacing:.2px;margin-bottom:5px}
.contact{display:flex;gap:10px;align-items:center;font-size:11.5px;font-weight:400}
.contact span{display:flex;align-items:center;gap:4px}
.contact svg{width:11px;height:11px}

.video-badge{position:absolute;border-radius:50%;background:radial-gradient(circle at 40% 35%,#fde07a,#f6bd12 60%,#e9a600);display:flex;flex-direction:column;align-items:center;justify-content:center;text-align:center;color:var(--white);font-weight:700;text-transform:uppercase;line-height:1.25;box-shadow:0 0 0 3px rgba(246,189,18,.35)}
.play{background:var(--white);border-radius:3px;display:flex;align-items:center;justify-content:center}
.play i{display:block;width:0;height:0;border-style:solid;border-color:transparent transparent transparent var(--gold)}

/* outside: flipped cover half */
.cover-half{position:absolute;left:0;top:0;width:461px;height:317px;transform:rotate(180deg);background:var(--paper);overflow:hidden}
.food-photo{position:absolute;right:0;top:0;width:240px;height:317px;background:radial-gradient(circle at 55% 45%,#f3e6c8 0%,#e2c48a 35%,#9a6b3e 65%,#c9c4bd 100%);clip-path:ellipse(100% 78% at 100% 40%)}
.event-info{position:absolute;left:8px;top:14px;width:200px}
.event-info h2{font-family:"Marcellus",serif;color:var(--navy);font-size:16px;line-height:1.1;letter-spacing:.5px}
.event-info .by{font-size:8px;color:var(--gold-text);margin-top:4px}
.event-info hr{border:0;border-top:1px dotted #b7b7b7;margin:8px 0 10px;width:135px}
.date-block{text-align:center;width:135px;margin-bottom:8px}
.date-block b{display:block;font-size:8px;color:var(--gold-text);font-weight:600}
.date-block span{font-size:8px;color:var(--navy)}
.venue-mark{width:135px;text-align:center;color:var(--navy);font-weight:700;font-size:10px;margin:4px 0 6px}
.venue-addr{width:135px;text-align:center;font-size:7.5px;color:var(--navy);line-height:1.3}

/* outside: host half */
.host-half{position:absolute;left:0;top:317px;width:461px;height:317px}
.host-swoosh{position:absolute;left:-60px;top:-40px;width:560px;height:330px;border-radius:50%;background:var(--white)}
.host-title{position:absolute;left:11px;top:23px;font-size:19px;color:var(--gold-text);letter-spacing:.5px}
.host-rule{position:absolute;left:11px;top:48px;width:175px;border-top:1px dotted #c9c9c9}
.host-bio{position:absolute;left:11px;top:57px;width:290px;font-size:8.4px;line-height:1.35;color:var(--ink)}
.host-bio p{margin-bottom:10px}
.host-photo{position:absolute;left:328px;top:8px;width:120px;height:120px;border-radius:50%;background:linear-gradient(160deg,#f4f4f4,#d9d9d9 60%,#2b2b2b 100%);border:5px solid #e4e4e4}
.host-name{position:absolute;left:318px;top:140px;width:140px;text-align:center;font-size:16px;color:var(--gold-text)}
.host-creds{position:absolute;left:318px;top:164px;width:140px;text-align:center;font-size:7.6px;color:var(--blue);line-height:1.35}
.press-row{position:absolute;left:13px;top:186px;display:flex;gap:9px;align-items:center}
.press-row i{display:block;height:16px;background:#c4c6cc;border-radius:2px}

/* inside */
.inside-head{position:absolute;left:0;top:34px;width:461px;text-align:center}
.inside-head h1{font-family:"Marcellus",serif;font-weight:400;color:var(--navy);font-size:20.5px;letter-spacing:.4px}
.inside-head p{font-family:"Marcellus",serif;color:var(--navy);font-size:13px;margin-top:2px}
.head-rule{position:absolute;left:14px;top:80px;width:433px;border-top:1px dotted #d8d0b0}
.invite{position:absolute;left:20px;top:92px;width:421px;text-align:center;font-size:8.6px;line-height:1.5}
.invite .note{margin-top:10px}
.enroll-ribbon{position:absolute;left:54px;top:180px;width:350px;height:33px;border-radius:17px;background:var(--gold-grad);color:var(--white);text-align:center;font-size:10.5px;font-weight:600;line-height:1.3;padding-top:3px;box-shadow:0 2px 4px rgba(0,0,0,.25)}
.choose{position:absolute;left:0;top:229px;width:461px;text-align:center;color:var(--gold);font-weight:600;font-size:10.5px}
.day{position:absolute;top:259px;width:120px;text-align:center;color:var(--white);font-weight:300;font-size:14.5px;line-height:1.25}
.day--tue{left:24px}
.day--wed{left:335px}
.day-divider{position:absolute;top:250px;height:75px;border-left:1px solid rgba(246,189,18,.7)}
.venue{position:absolute;left:136px;top:254px;width:190px;text-align:center;color:var(--white)}
.venue-name{display:inline-block;border:2px solid var(--white);border-radius:5px;padding:5px 8px;font-weight:700;font-size:11px;letter-spacing:.3px;margin-bottom:6px}
.venue-line{font-size:7.6px;line-height:1.3}
.topics-title{position:absolute;left:0;top:345px;width:461px;text-align:center;color:var(--navy);font-size:19px;letter-spacing:.5px}
.topics{position:absolute;left:10px;top:376px;width:441px;display:flex;justify-content:space-between}
.topic{width:106px;text-align:center}
.topic-img{width:90px;height:90px;margin:0 auto;border-radius:50%;border:5px solid #dcdde0}
.topic h4{margin-top:24px;font-weight:400;color:var(--blue);font-size:10px}
.topic p{margin-top:4px;font-size:7.4px;line-height:1.35;color:var(--ink)}
.footer-copy--right{left:auto;right:14px;text-align:right}
.footer-copy--right .contact{justify-content:flex-end}
</style>
</head>
<body>

<!-- Outside panel: flipped cover over host page -->
<section class="panel panel--outside">
  <div class="host-half">
    <div class="host-swoosh"></div>
    <h2 class="host-title serif">MEET YOUR HOST</h2>
    <div class="host-rule"></div>
    <div class="host-bio">
      <p>Dorian Vell an instructor at Westbrook College and a Certified Financial Planner. Dorian writes for the Harbor Street Ledger and is a regular guest on KVLM 980AM. As an instructor Dorian's focus is on teaching about smart retirement strategies that are unknown to most consumers.</p>
      <p>His lectures are focused on retirement, estate planning and advanced tax strategies. Dorian works exclusively with people ages 55-67 years old who are in retirement or focused on retiring.</p>
      <p>Dorian has been featured in the following and more:</p>
    </div>
    <div class="host-photo" role="img" aria-label="Portrait photo of host Dorian Vell"></div>
    <div class="host-name serif">Dorian Vell</div>
    <div class="host-creds">Certified Financial Planner<br>Instructor at Westbrook<br>Ledger Financial Writer</div>
    <div class="press-row" aria-label="Press features">
      <i style="width:34px"></i><i style="width:52px"></i><i style="width:46px"></i><i style="width:48px"></i><i style="width:20px;height:20px;border-radius:50%"></i>
    </div>
  </div>

  <div class="cover-half">
    <div class="food-photo" role="img" aria-label="Photo of a seafood pasta dish with mussels and lemon"></div>
    <div class="event-info">
      <h2>DINING &amp; RETIREMENT<br>EDUCATION</h2>
      <div class="by">By Westbrook Instructor Dorian Vell</div>
      <hr>
      <div class="date-block"><b>TUESDAY</b><span>October 8th at 7:00 pm</span></div>
      <div class="date-block"><b>WEDNESDAY</b><span>October 9th at 7:00 pm</span></div>
      <div class="venue-mark">Marlow's Tavern Grill</div>
      <div class="venue-addr">2870 Harbor Crest Blvd. #410<br>Bayview, CA 90000<br>(Floor 2)</div>
    </div>
    <svg class="footer-band" viewBox="0 0 461 80" preserveAspectRatio="none">
      <path d="M0 28 Q230 -6 461 22 L461 80 L0 80Z" fill="#1d3c84"/>
      <path d="M0 28 Q230 -6 461 22" fill="none" stroke="#f2b400" stroke-width="3"/>
    </svg>
    <div class="footer-copy">
      <h3>REGISTRATION IS LIMITED!</h3>
      <div class="contact">
        <span><svg viewBox="0 0 12 12"><circle cx="6" cy="6" r="5.2" fill="none" stroke="#fff"/><path d="M4 3.5l1 1-0.6 1 1.6 1.6 1-0.6 1 1-0.8 1C5.6 8.6 3.4 6.4 3.4 4.3z" fill="#fff"/></svg>888-555-0142 or visit</span>
        <span><svg viewBox="0 0 12 12"><path d="M6 1a3.5 3.5 0 0 1 3.5 3.5C9.5 7 6 11 6 11S2.5 7 2.5 4.5A3.5 3.5 0 0 1 6 1z" fill="#fff"/><circle cx="6" cy="4.5" r="1.3" fill="#1d3c84"/></svg>retireplanclass.org</span>
      </div>
    </div>
    <div class="video-badge" style="left:351px;top:213px;width:84px;height:84px;font-size:5.5px">
      <div class="play" style="width:20px;height:13px;margin-bottom:5px"><i style="border-width:3.5px 0 3.5px 6px"></i></div>
      View a video of<br>Dorian online &amp; register at<br>retireplanclass.org
    </div>
  </div>

  <svg class="footer-band" viewBox="0 0 461 80" preserveAspectRatio="none">
    <path d="M0 28 Q230 -6 461 22 L461 80 L0 80Z" fill="#1d3c84"/>
    <path d="M0 28 Q230 -6 461 22" fill="none" stroke="#f2b400" stroke-width="3"/>
  </svg>
  <div class="footer-copy">
    <h3>REGISTRATION IS LIMITED!</h3>
    <div class="contact">
      <span><svg viewBox="0 0 12 12"><circle cx="6" cy="6" r="5.2" fill="none" stroke="#fff"/><path d="M4 3.5l1 1-0.6 1 1.6 1.6 1-0.6 1 1-0.8 1C5.6 8.6 3.4 6.4 3.4 4.3z" fill="#fff"/></svg>888-555-0142 or visit</span>
      <span><svg viewBox="0 0 12 12"><path d="M6 1a3.5 3.5 0 0 1 3.5 3.5C9.5 7 6 11 6 11S2.5 7 2.5 4.5A3.5 3.5 0 0 1 6 1z" fill="#fff"/><circle cx="6" cy="4.5" r="1.3" fill="#1d3c84"/></svg>retireplanclass.org</span>
    </div>
  </div>
  <div class="video-badge" style="left:346px;top:532px;width:86px;height:86px;font-size:5.6px">
    <div class="play" style="width:20px;height:13px;margin-bottom:5px"><i style="border-width:3.5px 0 3.5px 6px"></i></div>
    View a video of<br>Dorian online &amp; register at<br>retireplanclass.org
  </div>
</section>

<!-- Inside panel -->
<section class="panel panel--inside">
  <svg class="abs" style="left:0;top:0" width="461" height="634" viewBox="0 0 461 634">
    <defs>
      <linearGradient id="goldLine" x1="0" x2="1"><stop offset="0" stop-color="#d99a00"/><stop offset=".5" stop-color="#fde89a"/><stop offset="1" stop-color="#e9a600"/></linearGradient>
    </defs>
    <rect x="0" y="0" width="461" height="6" fill="url(#goldLine)"/>
    <path d="M0 196 L461 196 L461 400 Q250 300 0 388Z" fill="#1d3c84"/>
    <path d="M461 400 Q250 300 0 388" fill="none" stroke="url(#goldLine)" stroke-width="4"/>
    <path d="M0 388 Q250 300 461 400 L461 420 Q250 320 0 405Z" fill="#f0f0f2"/>
  </svg>
  <div class="inside-head">
    <h1>ADVANCED RETIREMENT SOLUTIONS</h1>
    <p>Featuring Westbrook Instructor Dorian Vell, CFP</p>
  </div>
  <div class="head-rule"></div>
  <div class="invite">
    <p>You are invited to an educational talk featuring Westbrook Instructor Dorian Vell. This free* event is focused on teaching the techniques and tools that your financial advisor does not want you to know. Instructor Dorian Vell will cover advanced retirement and tax topics which are proven to be successful and mostly unknown to consumers.</p>
    <p class="note">Leave your checkbooks at home, there will be no selling here!</p>
  </div>
  <div class="enroll-ribbon">EARLY ENROLLMENT IS FREE.<br>Participants may enroll at door for $99 per seat.</div>
  <div class="choose">Choose from: Vegan, Vegetarian, Seafood, Pasta or Steak</div>
  <div class="day day--tue">TUESDAY<br>October 8th<br>at 7:00 pm</div>
  <div class="day-divider" style="left:136px"></div>
  <div class="venue">
    <div class="venue-name">Marlow's Tavern Grill</div>
    <div class="venue-line">2870 Harbor Crest Blvd. #410 Bayview,<br>CA 90000 (Floor 2)</div>
  </div>
  <div class="day-divider" style="left:324px"></div>
  <div class="day day--wed">WEDNESDAY<br>October 9th<br>at 7:00 pm</div>

  <h2 class="topics-title serif">TOPICS</h2>
  <div class="topics">
    <div class="topic">
      <div class="topic-img" role="img" aria-label="Photo of a calculator and financial charts" style="background:linear-gradient(150deg,#eef2f8,#aebfd8 60%,#6d7f9c)"></div>
      <h4>LOW-RISK INVESTING</h4>
      <p>New low-risk investments that produce 5%-7% interest and can provide you long term care income. (Not Stocks/Bonds)</p>
    </div>
    <div class="topic">
      <div class="topic-img" role="img" aria-label="Photo of a will document with a gavel and pen" style="background:linear-gradient(150deg,#f6f3ee,#d8c6a8 60%,#9a6a3a)"></div>
      <h4>ESTATE PLANNING</h4>
      <p>If you own a home, it's essential to have a Trust in order to avoid probate and to protect yourself if you become disabled.</p>
    </div>
    <div class="topic">
      <div class="topic-img" role="img" aria-label="Photo of a smiling retired couple" style="background:linear-gradient(150deg,#eef3f8,#d9c2a8 55%,#8fa6c0)"></div>
      <h4>TAX STRATEGIES</h4>
      <p>Learn how to save at least 30% on your 401k taxes and greatly reduce your taxable income in retirement.</p>
    </div>
    <div class="topic">
      <div class="topic-img" role="img" aria-label="Photo of a caregiver with an elderly woman" style="background:linear-gradient(150deg,#f4f6f8,#c9d4de 55%,#7a95b0)"></div>
      <h4>LONG TERM CARE</h4>
      <p>Learn how to protect yourself against the high costs of long-term care. Discover 3 new solutions you may not have seen before.</p>
    </div>
  </div>

  <svg class="footer-band" viewBox="0 0 461 80" preserveAspectRatio="none">
    <path d="M0 26 Q230 -6 461 14 L461 80 L0 80Z" fill="#1d3c84"/>
    <path d="M0 26 Q230 -6 461 14" fill="none" stroke="url(#goldLine)" stroke-width="3"/>
  </svg>
  <div class="footer-copy footer-copy--right">
    <h3>REGISTRATION IS LIMITED!</h3>
    <div class="contact">
      <span><svg viewBox="0 0 12 12"><circle cx="6" cy="6" r="5.2" fill="none" stroke="#fff"/><path d="M4 3.5l1 1-0.6 1 1.6 1.6 1-0.6 1 1-0.8 1C5.6 8.6 3.4 6.4 3.4 4.3z" fill="#fff"/></svg>888-555-0142 or visit</span>
      <span><svg viewBox="0 0 12 12"><path d="M6 1a3.5 3.5 0 0 1 3.5 3.5C9.5 7 6 11 6 11S2.5 7 2.5 4.5A3.5 3.5 0 0 1 6 1z" fill="#fff"/><circle cx="6" cy="4.5" r="1.3" fill="#1d3c84"/></svg>retireplanclass.org</span>
    </div>
  </div>
  <div class="video-badge" style="left:40px;top:562px;width:58px;height:58px;font-size:3.8px">
    <div class="play" style="width:14px;height:9px;margin-bottom:3px"><i style="border-width:2.5px 0 2.5px 4px"></i></div>
    View a video of<br>Dorian online &amp; register at<br>retireplanclass.org
  </div>
</section>

</body>
</html>
```